Full service meeting planning company needs new business cards

Velmora Linkway is a full service meeting planning company that specializes in on-line conference registration web development and event communications. We combine citywide hotel management, mobile applications, eblast reminders, confirmation letters, and customized reporting to create a seamless registration process. We also manage group motor coach transportation, food and beverages, entertainment, stage and lighting for group of 10 to 4000.

Target Market(s)

Corporations and associations

Industry/Entity Type

Event Planning

Contact Information for Business Card

standard size 3.5" wide and 2" tall

Font styles to use
Serif
Sans Serif

Colors
f37122
f78f20
333333
5c5c5c
9d9d9d
f68d4d

Requirements
Must have
• {name}
• Velmora Linkway
• P.O. Box 7384, Grand Rapids, M I 49568
• www.velmoralinkway.com
• {email}
• {phone}
• {mobile phone}
Nice to have
• Our colors are black, grey and orange as an accent color
Should not have
• I am not happy with our website layout anymore either. It feels dark and old but it does explain who we are pretty well if you'd like to review; www.velmoralinkway.com

```html
<!DOCTYPE html>
<html lang="en">
<head>
<meta charset="utf-8">
<title>Velmora Linkway – Business Cards</title>
<link rel="stylesheet" href="https://fonts.googleapis.com/css2?family=Roboto:wght@400;500&display=swap">
<style>
  :root {
    --orange: #f37122;
    --orange-light: #f78f20;
    --orange-soft: #f68d4d;
    --charcoal: #333333;
    --grey-dark: #5c5c5c;
    --grey: #9d9d9d;
    --white: #ffffff;
    --backdrop: #e9e7e4;
  }
  * { margin: 0; padding: 0; box-sizing: border-box; }
  html, body {
    width: 1200px;
    height: 588px;
    overflow: hidden;
    background: var(--backdrop);
    font-family: "Roboto", Arial, sans-serif;
  }
  .canvas {
    position: relative;
    width: 1200px;
    height: 588px;
    display: flex;
    align-items: center;
    justify-content: center;
    gap: 40px;
  }
  .card {
    position: relative;
    width: 540px;
    height: 309px;
    overflow: hidden;
    border-radius: 3px;
  }

  /* Contact side */
  .card--contact {
    background: linear-gradient(135deg, var(--orange) 0%, var(--orange-light) 100%);
  }
  .contact-band {
    position: absolute;
    inset: 0;
    width: 100%;
    height: 100%;
  }
  .contact-list {
    position: absolute;
    left: 22px;
    top: 26px;
    list-style: none;
    display: flex;
    flex-direction: column;
    gap: 17px;
  }
  .contact-item {
    display: flex;
    align-items: center;
    gap: 16px;
    color: var(--white);
    font-size: 22px;
    font-weight: 400;
    line-height: 1;
    white-space: nowrap;
  }
  .contact-icon {
    width: 28px;
    height: 28px;
    flex: none;
  }

  /* Brand side */
  .card--brand {
    background: var(--charcoal);
  }
  .brand-mark {
    position: absolute;
    left: 86px;
    top: 62px;
    width: 84px;
    height: 84px;
    border-radius: 50%;
    background: var(--orange);
  }
  .brand-name {
    position: absolute;
    left: 30px;
    top: 164px;
    color: var(--orange);
    font-size: 20px;
    font-weight: 500;
    letter-spacing: 0.3px;
    line-height: 1;
    text-transform: uppercase;
    white-space: nowrap;
  }
  .brand-dots {
    position: absolute;
    right: 26px;
    top: 196px;
    display: flex;
    gap: 18px;
  }
  .brand-dot {
    width: 64px;
    height: 64px;
    border-radius: 50%;
    background: var(--orange);
  }
</style>
</head>
<body>
<main class="canvas">

  <section class="card card--contact" aria-label="Contact side">
    <svg class="contact-band" viewBox="0 0 540 309" preserveAspectRatio="none" aria-hidden="true">
      <path d="M470 0 Q430 154 470 309 L540 309 L540 0 Z" fill="var(--grey-dark)"/>
      <path d="M470 0 Q430 154 470 309 L478 309 Q440 154 478 0 Z" fill="var(--grey)" opacity="0.6"/>
    </svg>
    <ul class="contact-list">
      <li class="contact-item">
        <svg class="contact-icon" viewBox="0 0 28 28" aria-hidden="true">
          <circle cx="14" cy="14" r="14" fill="var(--white)"/>
          <circle cx="14" cy="11" r="4" fill="var(--orange)"/>
          <path d="M7 21 Q14 12 21 21 Z" fill="var(--orange)"/>
        </svg>
        <span class="contact-label">Name</span>
      </li>
      <li class="contact-item">
        <svg class="contact-icon" viewBox="0 0 28 28" aria-hidden="true">
          <circle cx="14" cy="14" r="14" fill="var(--white)"/>
          <path d="M9 8 L12 8 L13 11.5 L11.3 12.8 Q12.8 15.6 15.2 16.7 L16.5 15 L20 16 L20 19 Q19 20.5 16.5 20 Q9.5 17.5 8 10.5 Q7.8 8.6 9 8 Z" fill="var(--orange)"/>
        </svg>
        <span class="contact-label">Phone</span>
      </li>
      <li class="contact-item">
        <svg class="contact-icon" viewBox="0 0 28 28" aria-hidden="true">
          <circle cx="14" cy="14" r="14" fill="var(--white)"/>
          <rect x="7" y="9" width="14" height="10" rx="1" fill="none" stroke="var(--orange)" stroke-width="1.8"/>
          <path d="M7.5 9.5 L14 15 L20.5 9.5" fill="none" stroke="var(--orange)" stroke-width="1.8"/>
        </svg>
        <span class="contact-label">Email</span>
      </li>
      <li class="contact-item">
        <svg class="contact-icon" viewBox="0 0 28 28" aria-hidden="true">
          <circle cx="14" cy="14" r="14" fill="var(--white)"/>
          <rect x="10" y="6" width="8" height="16" rx="1.5" fill="none" stroke="var(--orange)" stroke-width="1.8"/>
          <circle cx="14" cy="19" r="1" fill="var(--orange)"/>
        </svg>
        <span class="contact-label">Mobile phone</span>
      </li>
      <li class="contact-item">
        <svg class="contact-icon" viewBox="0 0 28 28" aria-hidden="true">
          <circle cx="14" cy="14" r="14" fill="var(--white)"/>
          <path d="M14 22 Q8 15 8 11.5 A6 6 0 0 1 20 11.5 Q20 15 14 22 Z" fill="var(--orange)"/>
          <circle cx="14" cy="11.5" r="2.2" fill="var(--white)"/>
        </svg>
        <span class="contact-label">Adress</span>
      </li>
      <li class="contact-item">
        <svg class="contact-icon" viewBox="0 0 28 28" aria-hidden="true">
          <circle cx="14" cy="14" r="14" fill="var(--white)"/>
          <circle cx="14" cy="14" r="7.5" fill="none" stroke="var(--orange)" stroke-width="1.5"/>
          <ellipse cx="14" cy="14" rx="3.2" ry="7.5" fill="none" stroke="var(--orange)" stroke-width="1.3"/>
          <path d="M6.5 14 H21.5" stroke="var(--orange)" stroke-width="1.3"/>
        </svg>
        <span class="contact-label">www.velmoralinkway.com</span>
      </li>
    </ul>
  </section>

  <section class="card card--brand" aria-label="Brand side">
    <div class="brand-mark" aria-hidden="true"></div>
    <p class="brand-name">Velmora Linkway</p>
    <div class="brand-dots" aria-hidden="true">
      <span class="brand-dot"></span>
      <span class="brand-dot"></span>
      <span class="brand-dot"></span>
    </div>
  </section>

</main>
</body>
</html>
```